CONDOMS Packaging Design Project

we are in need of the following:
1)a colorfull display box of 36 sales pack of 2 condoms with size when folded:
W=190mm,H=80mm,D=130mm
2)sales pack of 2 retangular foil condoms with sizes when folded:
Cover-W=60mm,H=62mm,D=12mm
drawer-W=59mm,H=61mm,D=11mm
The brand is VOLK,the UPC is WARM TIDE CONDOMS because it is benzocaine based to prolong the erection.
The sales pack packaging should be innovative,attractive,easy to open in the darkness,slim, thin,flat,12mm maximum as thickness for discretion,easy to be inserted into the pocket.

Our company logo,email,and other will be uploaded at final.
Only high qualified designers are welcome on this project.
Updates

Target Market(s)

15 to 35 years old men.

Industry/Entity Type

It Company

Requirements
Must have
• the sales pack of 2 condoms should be slim,thin,flat with 12mm of thickness for discretion but with hanger part to have the product visible at the reatail stores so if you can mix the 7x7 pack packaging with halvex packaging that will be great.the both packagings are in the attached files.
The design should have:
1)Map printing sales pack and display box.
2)map cutting sales pack and display box.
Nice to have
• The sales pack packaging should be innovative,attractive,easy to open in the darkness,slim and thin for discretion,easy to be inserted into the pocket,incisive colors to attract people.It will have 2 rectangular condoms foil inside.

The brand VOLK should be noted impressively like a merrovan and Castelvardo cars are for the public to penetrate the mind of the consumers as premium quality and assurance.
Should not have
• 1)avoid large size sales pack packaging.
2)avoid to exceed 12mm as thickness of the sales pack.

```html
<!DOCTYPE html>
<html lang="en">
<head>
<meta charset="utf-8">
<title>VOLK Warm Tide – sales pack fronts</title>
<link rel="stylesheet" href="https://fonts.googleapis.com/css2?family=Playfair+Display:wght@700;900&family=Roboto+Slab:wght@400;600;700&family=Josefin+Slab:wght@600;700&display=swap">
<style>
  :root {
    --canvas: #ffffff;
    --ink: #1b1b1f;
    --navy: #0f2148;
    --forest: #0f3d32;
    --peach-1: #f7a25a;
    --peach-2: #f6c3a8;
    --peach-3: #ee6f9a;
    --peach-4: #ffd65a;
    --sea-1: #2f8a78;
    --sea-2: #3d84c9;
    --sea-3: #6fc3d8;
    --sea-4: #1d4fb5;
    --lime: #bdf25f;
    --lime-ghost: #9cec92;
    --stone: #7a7a72;
    --tear-cut: #ffffff;
  }
  * { margin: 0; padding: 0; box-sizing: border-box; }
  html, body { width: 1200px; height: 1000px; overflow: hidden; background: var(--canvas); }
  .canvas { position: relative; width: 1200px; height: 1000px; }

  .pack {
    position: absolute; top: 110px; width: 340px; height: 760px;
    overflow: hidden; box-shadow: 0 8px 24px rgba(0,0,0,.12);
  }
  .pack--peach { left: 45px; }
  .pack--sea { left: 430px; }
  .pack--lime { left: 815px; background: var(--lime); }

  .pack__art { position: absolute; inset: 0; }
  .pack--peach .pack__art {
    background:
      radial-gradient(ellipse 70% 25% at 50% 38%, var(--peach-3) 0%, transparent 70%),
      radial-gradient(ellipse 80% 30% at 60% 85%, var(--peach-4) 0%, transparent 70%),
      linear-gradient(170deg, var(--peach-1) 0%, var(--peach-2) 45%, #f3a9b4 75%, #f6b37a 100%);
  }
  .pack--sea .pack__art {
    background:
      radial-gradient(circle at 30% 30%, var(--sea-3) 0%, transparent 40%),
      linear-gradient(165deg, var(--sea-1) 0%, var(--sea-2) 40%, var(--sea-3) 70%, var(--sea-4) 100%);
  }

  .pack__hanger { position: absolute; top: 0; left: 0; width: 340px; height: 140px; }

  .tear-line {
    position: absolute; left: 0; right: 0; top: 300px; height: 0;
    border-top: 3px dashed rgba(255,255,255,.8);
  }
  .tear-label {
    position: absolute; right: 14px; top: 272px;
    font: 600 16px/1 "Roboto Slab", serif; letter-spacing: 3px;
  }

  .ghost-name {
    position: absolute; font-family: "Playfair Display", serif; font-weight: 700;
    letter-spacing: 18px; white-space: nowrap; line-height: 1;
  }

  .brand { position: absolute; left: 0; right: 0; text-align: center;
    font-family: "Playfair Display", serif; font-weight: 900; line-height: 1; }
  .title { position: absolute; left: 0; right: 0; text-align: center;
    font-family: "Roboto Slab", serif; font-weight: 700; line-height: 1; }
  .claim { position: absolute; left: 0; right: 0; text-align: center;
    font-family: "Josefin Slab", serif; font-weight: 700; }
  .count { position: absolute; font-family: "Playfair Display", serif; font-weight: 700; line-height: 1; }
  .count-note { position: absolute; font-family: "Roboto Slab", serif; font-weight: 600; line-height: 1.05; }

  /* peach */
  .pack--peach .tear-label { color: #fff; }
  .pack--peach .ghost-name { top: 140px; left: -10px; font-size: 150px; color: rgba(255,255,255,.35); }
  .pack--peach .brand { top: 318px; font-size: 28px; color: #fff; letter-spacing: 3px; }
  .pack--peach .title { top: 440px; font-size: 32px; font-weight: 400; letter-spacing: 10px; color: var(--ink); }
  .pack--peach .claim { top: 495px; font-size: 20px; line-height: 1.1; color: #8a4b3a; letter-spacing: 2px; }
  .pack--peach .count { left: 40px; top: 640px; font-size: 72px; color: #fff; }
  .pack--peach .count-note { left: 92px; top: 650px; font-size: 18px; color: #fff; }

  /* sea */
  .pack--sea .tear-label { color: #fff; }
  .pack--sea .ghost-name { top: 300px; left: 10px; font-size: 80px; color: rgba(15,61,50,.35); }
  .pack--sea .brand { top: 300px; font-size: 36px; color: var(--forest); letter-spacing: 4px; }
  .pack--sea .title { top: 380px; font-size: 76px; letter-spacing: 12px; line-height: 1.05; color: var(--navy); }
  .pack--sea .claim { top: 560px; font-size: 16px; line-height: 1.1; color: var(--navy); letter-spacing: 1px; }
  .pack--sea .count { left: 50px; top: 650px; font-size: 72px; color: var(--ink); }
  .pack--sea .count-note { left: 100px; top: 645px; font-size: 22px; color: #dfe9f5; letter-spacing: 1px; }

  /* lime */
  .pack--lime .tear-label { color: var(--stone); font-size: 26px; top: 200px; }
  .pack--lime .ghost-name { top: 40px; left: -30px; font-size: 230px; color: var(--lime-ghost); letter-spacing: 0; }
  .pack--lime .ghost-name--low { top: 470px; left: 30px; }
  .pack--lime .brand { top: 320px; font-size: 66px; color: var(--stone); letter-spacing: 6px; }
  .pack--lime .title { top: 420px; font-size: 50px; letter-spacing: 10px; line-height: 1; color: var(--navy); }
  .pack--lime .claim { top: 530px; font-size: 25px; line-height: 1.05; color: var(--forest); letter-spacing: 2px; }
  .pack--lime .count { left: 40px; top: 620px; font-size: 110px; color: var(--navy); }
  .pack--lime .count-note { left: 30px; top: 728px; font-size: 16px; color: var(--forest); letter-spacing: 2px; }
</style>
</head>
<body>
<main class="canvas">

  <section class="pack pack--peach">
    <div class="pack__art" role="img" aria-label="Soft-focus close-up photograph in peach, pink and yellow tones"></div>
    <div class="ghost-name">VOLK</div>
    <svg class="pack__hanger" viewBox="0 0 340 140" aria-hidden="true">
      <path fill="var(--tear-cut)" d="M92 72 H145 A25 25 0 0 1 195 72 H248 A22 22 0 0 1 248 116 H92 A22 22 0 0 1 92 72 Z"/>
    </svg>
    <div class="tear-line"></div>
    <div class="tear-label">easy tear</div>
    <div class="brand">VOLK</div>
    <div class="title">WARM TIDE</div>
    <p class="claim">climax control lubricant<br>for longer lasting pleasure</p>
    <div class="count">2</div>
    <p class="count-note">individually<br>wrapped<br>condoms</p>
  </section>

  <section class="pack pack--sea">
    <div class="pack__art" role="img" aria-label="Mosaic pattern of green and blue hexagons"></div>
    <div class="ghost-name">VOLK</div>
    <svg class="pack__hanger" viewBox="0 0 340 140" aria-hidden="true">
      <path fill="var(--tear-cut)" d="M92 72 H145 A25 25 0 0 1 195 72 H248 A22 22 0 0 1 248 116 H92 A22 22 0 0 1 92 72 Z"/>
    </svg>
    <div class="tear-line"></div>
    <div class="tear-label">easy tear</div>
    <div class="brand">VOLK</div>
    <div class="title">WARM<br>TIDE</div>
    <p class="claim">climax control lubricant<br>for longer lasting pleasure</p>
    <div class="count">2</div>
    <p class="count-note">individually<br>wrapped<br>condoms</p>
  </section>

  <section class="pack pack--lime">
    <div class="ghost-name">VOLK</div>
    <div class="ghost-name ghost-name--low">VOLK</div>
    <svg class="pack__hanger" viewBox="0 0 340 140" aria-hidden="true">
      <path fill="var(--tear-cut)" d="M92 72 H145 A25 25 0 0 1 195 72 H248 A22 22 0 0 1 248 116 H92 A22 22 0 0 1 92 72 Z"/>
    </svg>
    <div class="tear-line"></div>
    <div class="tear-label">easy tear</div>
    <div class="brand">VOLK</div>
    <div class="title">WARM<br>TIDE</div>
    <p class="claim">climax control<br>lubricant<br>for longer lasting<br>pleasure</p>
    <div class="count">2</div>
    <p class="count-note">individually wrapped condoms</p>
  </section>

</main>
</body>
</html>
```